Bellwyn Strategic

Business Development Consulting Firm

Target Market(s)

Federal Government, 8(a) companies, Small Businesses

Industry/Entity Type

Private Sector, US Government

Contact Information for Business Card

8(a) Program Capture, Business Development, Industry Trends & Analysis, Strategic Teaming, Cyber Solutions

Colors

Designer to choose colors to be used in the design.

```html
<!DOCTYPE html>
<html lang="en">
<head>
<meta charset="utf-8">
<title>Bellwyn Strategic – Business Card</title>
<link rel="stylesheet" href="https://fonts.googleapis.com/css2?family=Roboto+Condensed:wght@400;700&display=swap">
<style>
  :root {
    --stage: #232323;
    --card-dark: #1f1f22;
    --brand-red: #ec1c24;
    --brand-red-deep: #d5141c;
    --brand-grey: #97989b;
    --ink-light: #ffffff;
    --rule: #bdbdbd;
  }
  * { box-sizing: border-box; margin: 0; padding: 0; }
  html, body { width: 1200px; height: 780px; overflow: hidden; }
  body {
    background: var(--stage);
    font-family: "Roboto Condensed", Arial, sans-serif;
    position: relative;
  }
  .card {
    position: absolute;
    top: 235px;
    width: 540px;
    height: 310px;
    overflow: hidden;
    box-shadow: 0 14px 30px rgba(0,0,0,.45);
  }

  /* Front: contact side */
  .card-front { left: 40px; background: var(--card-dark); }
  .front-brand {
    position: absolute; left: 48px; top: 72px;
    display: flex; align-items: center; gap: 12px;
  }
  .brand-dot {
    width: 34px; height: 34px; border-radius: 50%;
    background: var(--brand-red);
  }
  .front-brand .brand-name {
    font-weight: 700; font-size: 30px; letter-spacing: 1px;
    color: var(--brand-grey); text-transform: uppercase; line-height: 1;
  }
  .divider { position: absolute; left: 0; top: 0; pointer-events: none; }
  .contact {
    position: absolute; left: 318px; top: 118px; color: var(--ink-light);
  }
  .person-name { font-size: 29px; font-weight: 700; line-height: 1; }
  .person-name .first { color: var(--brand-red); }
  .person-role { font-size: 14px; margin: 4px 0 14px; }
  .contact-list { list-style: none; font-size: 14px; line-height: 1.55; }
  .contact-list li { display: flex; align-items: center; gap: 8px; }
  .contact-list svg { width: 12px; height: 12px; flex: none; }
  .address-band {
    position: absolute; left: 0; bottom: 24px;
    width: 410px; height: 32px; background: var(--brand-red);
    color: var(--ink-light); font-size: 14px;
    display: flex; align-items: center; padding-left: 40px;
  }
  .grey-band {
    position: absolute; left: 410px; bottom: 24px;
    width: 130px; height: 32px; background: var(--brand-grey);
  }
  .band-circle {
    position: absolute; left: 392px; bottom: 22px;
    width: 36px; height: 36px; border-radius: 50%;
    background: var(--card-dark); border: 4px solid var(--brand-red);
  }

  /* Back: brand side */
  .card-back {
    left: 620px;
    background: radial-gradient(circle at 60% 40%, #f0262d 0%, var(--brand-red) 45%, var(--brand-red-deep) 100%);
  }
  .back-pattern { position: absolute; inset: 0; }
  .back-brand {
    position: absolute; left: 0; right: 0; top: 108px;
    display: flex; justify-content: center; align-items: center; gap: 14px;
  }
  .back-brand .brand-dot { background: var(--ink-light); width: 40px; height: 40px; }
  .back-brand .brand-name {
    font-weight: 700; font-size: 40px; letter-spacing: 1.5px;
    color: var(--ink-light); text-transform: uppercase; line-height: 1;
  }
  .services {
    position: absolute; left: 0; right: 0; bottom: 66px;
    text-align: center; color: var(--ink-light); font-size: 13.5px; letter-spacing: .2px;
  }
</style>
</head>
<body>

  <section class="card card-front">
    <div class="front-brand">
      <span class="brand-dot"></span>
      <span class="brand-name">Bellwyn Strategic</span>
    </div>

    <svg class="divider" width="540" height="310" aria-hidden="true">
      <line x1="196" y1="244" x2="298" y2="132" stroke="var(--rule)" stroke-width="1"/>
    </svg>

    <div class="contact">
      <p class="person-name"><span class="first">Marta</span> Kovalin</p>
      <p class="person-role">Co-Founder</p>
      <ul class="contact-list">
        <li>
          <svg viewBox="0 0 24 24" aria-hidden="true"><path fill="var(--brand-red)" d="M6.6 10.8a15 15 0 0 0 6.6 6.6l2.2-2.2c.3-.3.7-.4 1-.2 1.1.4 2.300.6 3.6.6.6 0 1 .4 1 1V20c0 .6-.4 1-1 1A17 17 0 0 1 3 4c0-.6.4-1 1-1h3.5c.6 0 1 .4 1 1 0 1.3.2 2.5.6 3.6.1.3 0 .7-.2 1z"/></svg>
          (555) 204-3180
        </li>
        <li>
          <svg viewBox="0 0 24 24" aria-hidden="true"><path fill="var(--brand-red)" d="M2 5h20v14H2zm2 2v.5l8 5 8-5V7l-8 5z"/></svg>
          info@bellwynstrategic.com
        </li>
        <li>
          <svg viewBox="0 0 24 24" aria-hidden="true"><circle cx="12" cy="12" r="10" fill="var(--brand-red)"/><path d="M2 12h20M12 2c3 3 3 17 0 20M12 2c-3 3-3 17 0 20" stroke="var(--card-dark)" stroke-width="1.5" fill="none"/></svg>
          www.bellwynstrategic.com
        </li>
      </ul>
    </div>

    <div class="address-band">1840 Larkfield Ave. Suite 300 Fort Worth, TX 76104</div>
    <div class="grey-band"></div>
    <span class="band-circle"></span>
  </section>

  <section class="card card-back">
    <div class="back-pattern" role="img" aria-label="Faint repeating pattern of small arc shapes across the red background"></div>
    <div class="back-brand">
      <span class="brand-dot"></span>
      <span class="brand-name">Bellwyn Strategic</span>
    </div>
    <p class="services">Program Capture • Business Development • Industry Trends &amp; Analysis • Strategic Teaming</p>
  </section>

</body>
</html>
```